Rollvane Supply .com

This website is simple!!!
Landing page background image should capture the customers attention!!! We will provide a image as a example of what we like. The purpose for this website is to provide customers with a clean easy way to request a quote for industrial casters and wheels by OEM’s as well as maintenance departments worldwide. Please see if you can follow our thought process below.
Customer comes to website, they are invited to Request a Quote by providing us with Manufacturer Name, Manufacturers Part # and quantity needed.
If this is not known the customer will complete will WP conversation format form answering about 10 questions
Or
Look up the part number in one of the 8 to 12 catalogs located in the Pagewhirl Deck format on our catalog page, or equal plug in .
When the client request a quote a account page will pop up request The following:
Clients first and last name
Email address
And optional questions
Company name and best contact number.
Once this is complete customer will hit SUBMIT.
The customers request will be in system. A email will be sent to Customer service notifying us the Quote Request has been made.
We will then build a quote for the customer with a good, better and best options. Customers Request a Quote submission may have more than one caster or wheel requested at a time, so website must allow this.
When the customer comes back into website there email address will come up as the account name and request a password be made for them. This will allow them to store quotes in their account for future needs. If quote is older than 30 day the system will trigger a button at the bottom of the quote for resubmit Request for updated quote.
Once customer reviews quote the quote can be Converted to order within the website.
Once Converted the system will send us a email and order will be processed.
We will need a Chat program that will text to CS the questions.
You will need to have high quality graphic design skills on your team.
We have found 2 plugins that would work nicely with our new website Pagewhirl decks to showcase our catalogs for customers to research and QuillKit conversation forms to complete request for quote form.
Just Ideas:
Very very ghosted caster blueprint in white background but very very ghosted or the icon just idea
We have never had a font used we like
Grayscale every except for rubber on wheels and logo icon
Website should have hamburger menu on left
Website should hav responsive deign
Account head on right side
Has anyone read the brief from top to bottom and the updates, I’m seeing a lot of duplicates of the website I posted in images I want a clean website With lite backgrand with the poly being definite colors on each wheel I added a green yellow and red image has anyone looked at that Just a question?
Went on vacation/holiday

```html
<!DOCTYPE html>
<html lang="en">
<head>
<meta charset="utf-8">
<title>Rollvane Supply .com — Homepage Concepts</title>
<link href="https://fonts.googleapis.com/css2?family=Montserrat:wght@400;500;600;700;800&display=swap" rel="stylesheet">
<style>
:root{
  --stage:#d8d8d8;
  --blue:#3c7ede;
  --navy:#1b3f9d;
  --ink:#1d1d1d;
  --muted:#6a6a6a;
  --line:#dcdcdc;
  --white:#ffffff;
  --tint:#f2f3f5;
  --tint-blue:#e6eaf3;
  --footer:#242424;
  --footer-text:#cfcfcf;
}
*{box-sizing:border-box;margin:0;padding:0}
html,body{width:840px;height:1200px;overflow:hidden}
body{background:var(--stage);font-family:'Montserrat',sans-serif;color:var(--ink);position:relative}
.page{position:absolute;top:36px;width:595px;height:2158px;background:var(--white);transform:scale(0.5227);transform-origin:0 0;overflow:hidden}
.page--photo{left:67px}
.page--light{left:462px}
.section{position:absolute;left:0;width:595px}
.abs{position:absolute}

/* buttons */
.btn{position:absolute;height:28px;border-radius:14px;font-size:8px;font-weight:500;letter-spacing:.3px;display:flex;align-items:center;justify-content:center;text-transform:uppercase}
.btn--primary{background:var(--blue);color:var(--white)}
.btn--ghost{background:var(--white);color:var(--ink)}
.btn--outline{background:var(--white);color:var(--ink);border:1px solid #bbb}

/* hero */
.hero{top:0;height:356px;overflow:hidden}
.page--light .hero{height:368px;background:linear-gradient(135deg,#f7f7f7 0%,#ececec 60%,#f4f4f4 100%)}
.hero__photo{position:absolute;inset:0;background:radial-gradient(ellipse at 72% 55%,#4f6f9e 0%,#34465f 22%,#2a2a2a 48%,#1a1a1a 70%),#1a1a1a}
.hero__photo::after{content:"";position:absolute;left:0;right:0;bottom:0;height:120px;background:linear-gradient(180deg,rgba(120,120,120,0) 0%,#8a8a8a 100%)}
.hero__products{position:absolute;left:300px;top:55px;width:290px;height:300px;border-radius:40%;background:radial-gradient(circle at 35% 38%,#2d3b63 0%,#26304e 28%,rgba(40,40,40,.0) 60%),radial-gradient(circle at 70% 75%,#2a3a66 0%,#273358 26%,rgba(200,200,200,0) 55%),radial-gradient(circle at 72% 22%,#3a3a3a 0%,#2b2b2b 22%,rgba(200,200,200,0) 45%)}
.menu-btn{position:absolute;left:36px;top:24px;width:24px;height:24px;border-radius:50%;background:var(--white);display:flex;align-items:center;justify-content:center;box-shadow:0 1px 3px rgba(0,0,0,.25)}
.brand{position:absolute;left:68px;top:52px;font-size:8.5px;font-weight:700;letter-spacing:.4px;white-space:nowrap}
.page--photo .hero .brand{color:var(--white)}
.page--light .hero .brand{color:var(--navy)}
.brand__dot{display:inline-block;width:7px;height:7px;border-radius:50%;background:currentColor;margin-right:4px;vertical-align:-0.5px}
.phone{position:absolute;left:345px;top:24px;font-size:8.5px;font-weight:500;display:flex;align-items:center;gap:3px}
.page--photo .phone{color:var(--white)}
.page--light .phone{color:var(--ink)}
.login{position:absolute;left:447px;top:16px;width:93px;height:26px;border-radius:13px;background:var(--blue);color:var(--white);font-size:7px;font-weight:500;display:flex;align-items:center;justify-content:center;gap:3px}
.hero__title{position:absolute;left:55px;top:124px;font-size:27px;line-height:35px;font-weight:800;letter-spacing:.3px}
.page--photo .hero__title{color:var(--white)}
.page--light .hero__title{color:var(--ink)}

/* headings */
.h2{font-size:19.5px;line-height:26px;font-weight:700;letter-spacing:.2px;text-transform:uppercase}
.h2--center{position:absolute;left:0;width:595px;text-align:center}
.body{font-size:7px;line-height:13.5px;color:var(--muted)}

/* welcome */
.welcome{top:356px;height:281px}
.page--light .welcome{top:368px;height:269px}
.feature{position:absolute;left:357px;display:flex;align-items:center;gap:20px}
.feature__text{font-size:10px;line-height:14px;font-weight:500;color:var(--ink)}

/* featured */
.featured{top:637px;height:281px;background:linear-gradient(120deg,#f6f6f6 0%,#eeeeee 50%,#f8f8f8 100%)}
.page--light .featured{background:linear-gradient(120deg,#e4e8f1 0%,#edf0f6 55%,#e6eaf2 100%)}
.card{position:absolute;top:87px;width:114px;height:122px;background:var(--white);box-shadow:0 2px 6px rgba(0,0,0,.08)}
.card__img{position:absolute;left:17px;top:12px;width:80px;height:98px;border-radius:45%}
.card__caption{position:absolute;top:220px;width:120px;font-size:7px;line-height:12px;color:#333}
.arrow{position:absolute;top:141px}

/* tech */
.tech{top:918px;height:378px}
.tech__drawing{position:absolute;left:35px;top:40px;width:275px;height:225px;background:linear-gradient(180deg,#f4f4f4,#ececec)}
.acc{position:absolute;left:346px;width:194px;display:flex;justify-content:space-between;align-items:center;font-size:9px;font-weight:500;color:var(--ink)}
.chev{width:14px;height:14px;border-radius:50%;border:1px solid #999;display:flex;align-items:center;justify-content:center}
.dims{position:absolute;left:346px;top:160px;font-size:7px;line-height:12.8px;color:var(--muted)}

/* steps */
.steps{top:1296px;height:302px;background:linear-gradient(135deg,#1d44a6 0%,#1a3c98 50%,#1e45a8 100%);color:var(--white)}
.step{position:absolute;top:79px;width:170px;text-align:center}
.step__ring{margin:0 auto;width:92px;height:92px;border-radius:50%;border:1.5px solid rgba(255,255,255,.55);display:flex;align-items:center;justify-content:center;position:relative}
.step__num{position:absolute;left:37px;bottom:-9px;width:18px;height:18px;border-radius:50%;background:#6f88c9;font-size:8.5px;font-weight:600;display:flex;align-items:center;justify-content:center}
.step__label{margin-top:20px;font-size:10.5px;font-weight:500}

/* blog */
.blog{top:1598px;height:357px}
.post{position:absolute;top:81px;width:154px}
.post__img{width:154px;height:86px}
.post__title{margin-top:40px;font-size:10px;line-height:13px;font-weight:500;color:var(--ink)}
.post__meta{margin-top:9px;font-size:6.5px;color:#444;display:flex;align-items:center;gap:2px}
.post__meta b{color:var(--blue);font-weight:400}
.post__text{margin-top:9px;font-size:7px;line-height:12.5px;color:var(--muted)}
.post__more{margin-top:7px;font-size:7.5px;font-weight:500;color:var(--blue);text-transform:uppercase}

/* footer */
.footer{top:1955px;height:203px;background:var(--footer);color:var(--footer-text)}
.footer .brand{left:55px;top:92px;color:var(--white);font-size:11px}
.footer .brand .brand__dot{width:9px;height:9px}
.f-col{position:absolute;top:29px}
.f-col h4{font-size:8.5px;font-weight:600;color:var(--white);margin-bottom:9px}
.f-col li{list-style:none;font-size:7px;line-height:15.3px}
.f-contact{display:flex;gap:6px;font-size:7px;line-height:11.5px;margin-bottom:12px;width:160px}
.f-rule{position:absolute;left:55px;top:155px;width:485px;height:1px;background:#444}
.copy{position:absolute;left:55px;top:173px;font-size:7px}
.social{position:absolute;top:169px;width:18px;height:18px;border-radius:50%;border:1px solid #9a9a9a}
</style>
</head>
<body>

<!-- ============ CONCEPT A : photographic hero ============ -->
<main class="page page--photo">
  <header class="section hero">
    <div class="hero__photo" role="img" aria-label="Close-up photograph of a blue caster wheel under a cart on carpet"></div>
    <span class="menu-btn"><svg width="11" height="9" viewBox="0 0 11 9"><path d="M0 1h11M3 4.5h8M0 8h11" stroke="#222" stroke-width="1.4"/></svg></span>
    <div class="brand"><span class="brand__dot"></span>ROLLVANE SUPPLY .com</div>
    <div class="phone"><svg width="8" height="8" viewBox="0 0 10 10"><path d="M2 0.5l2 2-1 1.3c.6 1.3 1.6 2.3 2.9 2.9L7.2 5.7l2.3 2-1.2 1.8C4.5 9.3 0.7 5.5 0.5 1.7z" fill="currentColor"/></svg>1 800 555 0142</div>
    <div class="login"><svg width="7" height="7" viewBox="0 0 10 10"><circle cx="5" cy="3" r="2.4" fill="#fff"/><path d="M0.5 10c0-3 2-4.5 4.5-4.5s4.5 1.5 4.5 4.5z" fill="#fff"/></svg>LOGIN/SIGN UP</div>
    <h1 class="hero__title">SOLUTIONS<br>FOR ALL YOUR<br>APPLICATIONS</h1>
    <span class="btn btn--primary" style="left:55px;top:248px;width:105px">Request a quote</span>
    <span class="btn btn--ghost" style="left:166px;top:248px;width:92px">Catalog</span>
  </header>

  <section class="section welcome">
    <h2 class="h2 abs" style="left:55px;top:39px">Welcome to<br>Rollvane Supply</h2>
    <p class="body abs" style="left:55px;top:98px;width:250px">Lorem ipsum dolor sit amet, consectetur adipiscing elit, sed do eiusmod tempor incididunt ut.</p>
    <p class="body abs" style="left:55px;top:138px;width:250px">Labore et dolore magna aliqua. Ut enim ad minim veniamqu is nostrud exercitation ullamco laboris nisi ut aliquip ex ea co mmodo consequat. Duis aute irure dolor in reprehenderit in voluptate velit esse cillum dolore eu.</p>
    <span class="btn btn--primary" style="left:55px;top:212px;width:82px">Read more</span>
    <div class="feature" style="top:40px"><svg width="42" height="42" viewBox="0 0 42 42" fill="none" stroke="#1b3f9d" stroke-width="1.6"><circle cx="23" cy="23" r="11"/><circle cx="23" cy="23" r="6"/><path d="M21 20l5 3-5 3z" fill="#3c7ede" stroke="none"/><circle cx="8" cy="8" r="4"/><path d="M16 4h10l4 4"/></svg><span class="feature__text">Advanced production<br>testing equipment</span></div>
    <div class="feature" style="top:105px"><svg width="42" height="46" viewBox="0 0 42 46" fill="none" stroke="#1b3f9d" stroke-width="1.6"><path d="M10 4h22M14 4v8h14V4"/><path d="M17 12l-3 14M25 12l3 14"/><circle cx="21" cy="33" r="9"/><circle cx="21" cy="33" r="4" stroke="#3c7ede"/></svg><span class="feature__text">High-quality<br>Products</span></div>
    <div class="feature" style="top:170px"><svg width="42" height="46" viewBox="0 0 42 46" fill="none" stroke="#1b3f9d" stroke-width="1.6"><circle cx="10" cy="8" r="4"/><circle cx="21" cy="6" r="4"/><circle cx="32" cy="8" r="4"/><circle cx="21" cy="30" r="10"/><circle cx="21" cy="30" r="4" stroke="#3c7ede"/></svg><span class="feature__text">Quality management<br>system</span></div>
  </section>

  <section class="section featured">
    <h2 class="h2 h2--center" style="top:33px">Featured products</h2>
    <svg class="arrow" style="left:32px" width="8" height="14" viewBox="0 0 8 14"><path d="M7 1L1 7l6 6" stroke="#333" fill="none" stroke-width="1.4"/></svg>
    <svg class="arrow" style="left:556px" width="8" height="14" viewBox="0 0 8 14"><path d="M1 1l6 6-6 6" stroke="#333" fill="none" stroke-width="1.4"/></svg>
    <div class="card" style="left:55px"><div class="card__img" role="img" aria-label="Swivel caster with navy wheel" style="background:radial-gradient(circle at 45% 65%,#2b3a63 0%,#2b3a63 35%,#c9c9c9 60%,#fff 72%)"></div></div>
    <div class="card" style="left:178px"><div class="card__img" role="img" aria-label="Black cast iron V-groove wheel" style="background:radial-gradient(circle,#2d2d2d 0%,#2a2a2a 55%,#fff 68%)"></div></div>
    <div class="card" style="left:301px"><div class="card__img" role="img" aria-label="Swivel caster with red and grey wheel and brake" style="background:radial-gradient(circle at 50% 62%,#6b6b6b 0%,#b32424 42%,#d6d6d6 60%,#fff 72%)"></div></div>
    <div class="card" style="left:424px"><div class="card__img" role="img" aria-label="Green polyurethane wheel" style="background:radial-gradient(circle,#b5b5b5 0%,#1e5b32 22%,#1e5b32 55%,#fff 68%)"></div></div>
    <p class="card__caption" style="left:55px">Duis aute irure dolor inrep rehenderit in volu..</p>
    <p class="card__caption" style="left:178px">Duis aute irure dolor inrep rehenderit in volu..</p>
    <p class="card__caption" style="left:301px">Duis aute irure dolor inrep rehenderit in volu..</p>
    <p class="card__caption" style="left:424px">Duis aute irure dolor inrep rehenderit in volu..</p>
  </section>

  <section class="section tech">
    <div class="tech__drawing" role="img" aria-label="Technical line drawings of a swivel caster in side, top and front views"></div>
    <h2 class="h2 abs" style="left:346px;top:42px">Technical<br>specification</h2>
    <p class="body abs" style="left:346px;top:102px;width:200px">Lorem ipsum dolor sit amet, consectetur adipis cing elit, sed do eiusmod tempor.</p>
    <div class="acc" style="top:143px">Dimensions<span class="chev"><svg width="6" height="4" viewBox="0 0 6 4"><path d="M0.5 3.5L3 1l2.5 2.5" stroke="#555" fill="none"/></svg></span></div>
    <div class="dims">Width: 700 mm<br>Height: 380 mm<br>Length: 900 mm<br>Front wheel diameter: 360 mm<br>Rear wheel diameter: 160 mm<br>Weight: 40 kg</div>
    <div class="acc" style="top:245px">Features<span class="chev"><svg width="6" height="4" viewBox="0 0 6 4"><path d="M0.5 0.5L3 3l2.5-2.5" stroke="#555" fill="none"/></svg></span></div>
    <div class="acc" style="top:270px">Power supply<span class="chev"><svg width="6" height="4" viewBox="0 0 6 4"><path d="M0.5 0.5L3 3l2.5-2.5" stroke="#555" fill="none"/></svg></span></div>
    <div class="acc" style="top:295px">Inputs and outputs<span class="chev"><svg width="6" height="4" viewBox="0 0 6 4"><path d="M0.5 0.5L3 3l2.5-2.5" stroke="#555" fill="none"/></svg></span></div>
    <div class="acc" style="top:321px">API<span class="chev"><svg width="6" height="4" viewBox="0 0 6 4"><path d="M0.5 0.5L3 3l2.5-2.5" stroke="#555" fill="none"/></svg></span></div>
  </section>

  <section class="section steps">
    <h2 class="h2 h2--center" style="top:40px">Three easy steps</h2>
    <div class="step" style="left:53px"><div class="step__ring"><svg width="40" height="40" viewBox="0 0 40 40" fill="none" stroke="#fff" stroke-width="1.5"><circle cx="15" cy="16" r="6"/><path d="M4 36c0-7 5-11 11-11s11 4 11 11"/><rect x="24" y="4" width="13" height="10" rx="1"/><path d="M27 8h7M27 11h5"/></svg><span class="step__num">1</span></div><p class="step__label">Request a Quote</p></div>
    <div class="step" style="left:212px"><div class="step__ring"><svg width="40" height="40" viewBox="0 0 40 40" fill="none" stroke="#fff" stroke-width="1.5"><rect x="3" y="7" width="34" height="22" rx="2"/><path d="M3 9l17 12 17-12"/><circle cx="20" cy="30" r="7" fill="#1b3f9d"/><path d="M20 26v7M17 30l3 3 3-3"/></svg><span class="step__num">2</span></div><p class="step__label">Receive a Quote</p></div>
    <div class="step" style="left:382px"><div class="step__ring"><svg width="40" height="40" viewBox="0 0 40 40" fill="none" stroke="#fff" stroke-width="1.5"><rect x="18" y="4" width="18" height="26" rx="1"/><path d="M22 12h10M22 17h10M22 22h8"/><path d="M4 20l8-4 8 4v10l-8 4-8-4z" fill="#1b3f9d"/><path d="M4 20l8 4 8-4M12 24v10"/></svg><span class="step__num">3</span></div><p class="step__label">Convert a Quote to order</p></div>
    <span class="btn btn--primary" style="left:196px;top:230px;width:104px">Request a quote</span>
    <span class="btn btn--ghost" style="left:311px;top:230px;width:92px">Catalog</span>
  </section>

  <section class="section blog">
    <h2 class="h2 h2--center" style="top:40px">Latest blog</h2>
    <article class="post" style="left:55px"><div class="post__img" role="img" aria-label="Angle grinder throwing sparks in a workshop" style="background:linear-gradient(120deg,#3b3b3b,#8a8a8a 45%,#d9a25a 62%,#3a3a3a)"></div><h3 class="post__title">At vero eos et accusamus et iusto odio dignis</h3><p class="post__meta"><b>&#9679;</b> 15/02/2022 &nbsp;|&nbsp; <b>&#9632;</b> Mara Quill</p><p class="post__text">Neque porro quisquam est, qui dolo rem ipsum quia dolor sit amet, cons ectetam est, qturdipisci.</p><p class="post__more">Read more</p></article>
    <article class="post" style="left:220px"><div class="post__img" role="img" aria-label="Blue caster wheels stacked on a shelf" style="background:linear-gradient(110deg,#2a2a2a,#b32a2a 30%,#3a6fd8 55%,#2f5fc4 80%,#6a6a6a)"></div><h3 class="post__title">At vero eos et accusamus et iusto odio dignis</h3><p class="post__meta"><b>&#9679;</b> 15/02/2022 &nbsp;|&nbsp; <b>&#9632;</b> Mara Quill</p><p class="post__text">Neque porro quisquam est, qui dolo rem ipsum quia dolor sit amet, cons ectetam est, qturdipisci.</p><p class="post__more">Read more</p></article>
    <article class="post" style="left:385px"><div class="post__img" role="img" aria-label="Fixed caster on a cart over a yellow floor line" style="background:linear-gradient(180deg,#8d8d8d,#c8c8c8 55%,#d8c640 80%,#e8e8e8)"></div><h3 class="post__title">At vero eos et accusamus et iusto odio dignis</h3><p class="post__meta"><b>&#9679;</b> 15/02/2022 &nbsp;|&nbsp; <b>&#9632;</b> Mara Quill</p><p class="post__text">Neque porro quisquam est, qui dolo rem ipsum quia dolor sit amet, cons ectetam est, qturdipisci.</p><p class="post__more">Read more</p></article>
  </section>

  <footer class="section footer">
    <div class="brand"><span class="brand__dot"></span>ROLLVANE SUPPLY .com</div>
    <div class="f-col" style="left:259px"><h4>Quick Links</h4><ul><li>Home</li><li>Contact Us</li><li>About</li><li>Resources</li><li>Blog</li><li>Privacy Policy</li></ul></div>
    <div class="f-col" style="left:377px"><h4>Contact Us</h4>
      <div class="f-contact"><svg width="6" height="8" viewBox="0 0 6 8"><path d="M3 0a3 3 0 0 1 3 3c0 2-3 5-3 5S0 5 0 3a3 3 0 0 1 3-3z" fill="#3c7ede"/></svg><span>At vero eos et accusamus et iust dignissimos ducimus qu</span></div>
      <div class="f-contact"><svg width="7" height="7" viewBox="0 0 10 10"><path d="M2 0.5l2 2-1 1.3c.6 1.3 1.6 2.3 2.9 2.9L7.2 5.7l2.3 2-1.2 1.8C4.5 9.3 0.7 5.5 0.5 1.7z" fill="#3c7ede"/></svg><span>1 800 555 0142</span></div>
      <div class="f-contact"><svg width="8" height="6" viewBox="0 0 8 6"><rect width="8" height="6" fill="#3c7ede"/><path d="M0 0l4 3 4-3" stroke="#242424" fill="none" stroke-width=".8"/></svg><span>info@rollvanesupply.com</span></div>
    </div>
    <div class="f-rule"></div>
    <p class="copy">©2022 Rollvane Supply. All rights reserved.</p>
    <span class="social" style="left:474px"></span><span class="social" style="left:497px"></span><span class="social" style="left:520px"></span>
  </footer>
</main>

<!-- ============ CONCEPT B : light hero ============ -->
<main class="page page--light">
  <header class="section hero">
    <div class="hero__products" role="img" aria-label="Group of three industrial casters and wheels with navy and black treads"></div>
    <span class="menu-btn"><svg width="11" height="9" viewBox="0 0 11 9"><path d="M0 1h11M3 4.5h8M0 8h11" stroke="#222" stroke-width="1.4"/></svg></span>
    <div class="brand"><span class="brand__dot"></span>ROLLVANE SUPPLY .com</div>
    <div class="phone"><svg width="8" height="8" viewBox="0 0 10 10"><path d="M2 0.5l2 2-1 1.3c.6 1.3 1.6 2.3 2.9 2.9L7.2 5.7l2.3 2-1.2 1.8C4.5 9.3 0.7 5.5 0.5 1.7z" fill="#3c7ede"/></svg>1 800 555 0142</div>
    <div class="login"><svg width="7" height="7" viewBox="0 0 10 10"><circle cx="5" cy="3" r="2.4" fill="#fff"/><path d="M0.5 10c0-3 2-4.5 4.5-4.5s4.5 1.5 4.5 4.5z" fill="#fff"/></svg>LOGIN/SIGN UP</div>
    <h1 class="hero__title" style="top:126px">SOLUTIONS<br>FOR ALL YOUR<br>APPLICATIONS</h1>
    <span class="btn btn--primary" style="left:55px;top:248px;width:105px">Request a quote</span>
    <span class="btn btn--outline" style="left:166px;top:248px;width:92px">Catalog</span>
  </header>

  <section class="section welcome">
    <h2 class="h2 abs" style="left:55px;top:27px">Welcome to<br>Rollvane Supply</h2>
    <p class="body abs" style="left:55px;top:86px;width:250px">Lorem ipsum dolor sit amet, consectetur adipiscing elit, sed do eiusmod tempor incididunt ut.</p>
    <p class="body abs" style="left:55px;top:126px;width:250px">Labore et dolore magna aliqua. Ut enim ad minim veniamqu is nostrud exercitation ullamco laboris nisi ut aliquip ex ea co mmodo consequat. Duis aute irure dolor in reprehenderit in voluptate velit esse cillum dolore eu.</p>
    <span class="btn btn--primary" style="left:55px;top:200px;width:82px">Read more</span>
    <div class="feature" style="top:28px"><svg width="42" height="42" viewBox="0 0 42 42" fill="none" stroke="#1b3f9d" stroke-width="1.6"><circle cx="23" cy="23" r="11"/><circle cx="23" cy="23" r="6"/><path d="M21 20l5 3-5 3z" fill="#3c7ede" stroke="none"/><circle cx="8" cy="8" r="4"/><path d="M16 4h10l4 4"/></svg><span class="feature__text">Advanced production<br>testing equipment</span></div>
    <div class="feature" style="top:93px"><svg width="42" height="46" viewBox="0 0 42 46" fill="none" stroke="#1b3f9d" stroke-width="1.6"><path d="M10 4h22M14 4v8h14V4"/><path d="M17 12l-3 14M25 12l3 14"/><circle cx="21" cy="33" r="9"/><circle cx="21" cy="33" r="4" stroke="#3c7ede"/></svg><span class="feature__text">High-quality<br>Products</span></div>
    <div class="feature" style="top:158px"><svg width="42" height="46" viewBox="0 0 42 46" fill="none" stroke="#1b3f9d" stroke-width="1.6"><circle cx="10" cy="8" r="4"/><circle cx="21" cy="6" r="4"/><circle cx="32" cy="8" r="4"/><circle cx="21" cy="30" r="10"/><circle cx="21" cy="30" r="4" stroke="#3c7ede"/></svg><span class="feature__text">Quality management<br>system</span></div>
  </section>

  <section class="section featured">
    <h2 class="h2 h2--center" style="top:33px">Featured products</h2>
    <svg class="arrow" style="left:32px" width="8" height="14" viewBox="0 0 8 14"><path d="M7 1L1 7l6 6" stroke="#333" fill="none" stroke-width="1.4"/></svg>
    <svg class="arrow" style="left:556px" width="8" height="14" viewBox="0 0 8 14"><path d="M1 1l6 6-6 6" stroke="#333" fill="none" stroke-width="1.4"/></svg>
    <div class="card" style="left:55px"><div class="card__img" role="img" aria-label="Swivel caster with navy wheel" style="background:radial-gradient(circle at 45% 65%,#2b3a63 0%,#2b3a63 35%,#c9c9c9 60%,#fff 72%)"></div></div>
    <div class="card" style="left:178px"><div class="card__img" role="img" aria-label="Black cast iron V-groove wheel" style="background:radial-gradient(circle,#2d2d2d 0%,#2a2a2a 55%,#fff 68%)"></div></div>
    <div class="card" style="left:301px"><div class="card__img" role="img" aria-label="Swivel caster with red and grey wheel and brake" style="background:radial-gradient(circle at 50% 62%,#6b6b6b 0%,#b32424 42%,#d6d6d6 60%,#fff 72%)"></div></div>
    <div class="card" style="left:424px"><div class="card__img" role="img" aria-label="Green polyurethane wheel" style="background:radial-gradient(circle,#b5b5b5 0%,#1e5b32 22%,#1e5b32 55%,#fff 68%)"></div></div>
    <p class="card__caption" style="left:55px">Duis aute irure dolor inrep rehenderit in volu..</p>
    <p class="card__caption" style="left:178px">Duis aute irure dolor inrep rehenderit in volu..</p>
    <p class="card__caption" style="left:301px">Duis aute irure dolor inrep rehenderit in volu..</p>
    <p class="card__caption" style="left:424px">Duis aute irure dolor inrep rehenderit in volu..</p>
  </section>

  <section class="section tech">
    <div class="tech__drawing" role="img" aria-label="Technical line drawings of a swivel caster in side, top and front views"></div>
    <h2 class="h2 abs" style="left:346px;top:42px">Technical<br>specification</h2>
    <p class="body abs" style="left:346px;top:102px;width:200px">Lorem ipsum dolor sit amet, consectetur adipis cing elit, sed do eiusmod tempor.</p>
    <div class="acc" style="top:143px">Dimensions<span class="chev"><svg width="6" height="4" viewBox="0 0 6 4"><path d="M0.5 3.5L3 1l2.5 2.5" stroke="#555" fill="none"/></svg></span></div>
    <div class="dims">Width: 700 mm<br>Height: 380 mm<br>Length: 900 mm<br>Front wheel diameter: 360 mm<br>Rear wheel diameter: 160 mm<br>Weight: 40 kg</div>
    <div class="acc" style="top:245px">Features<span class="chev"><svg width="6" height="4" viewBox="0 0 6 4"><path d="M0.5 0.5L3 3l2.5-2.5" stroke="#555" fill="none"/></svg></span></div>
    <div class="acc" style="top:270px">Power supply<span class="chev"><svg width="6" height="4" viewBox="0 0 6 4"><path d="M0.5 0.5L3 3l2.5-2.5" stroke="#555" fill="none"/></svg></span></div>
    <div class="acc" style="top:295px">Inputs and outputs<span class="chev"><svg width="6" height="4" viewBox="0 0 6 4"><path d="M0.5 0.5L3 3l2.5-2.5" stroke="#555" fill="none"/></svg></span></div>
    <div class="acc" style="top:321px">API<span class="chev"><svg width="6" height="4" viewBox="0 0 6 4"><path d="M0.5 0.5L3 3l2.5-2.5" stroke="#555" fill="none"/></svg></span></div>
  </section>

  <section class="section steps">
    <h2 class="h2 h2--center" style="top:40px">Three easy steps</h2>
    <div class="step" style="left:53px"><div class="step__ring"><svg width="40" height="40" viewBox="0 0 40 40" fill="none" stroke="#fff" stroke-width="1.5"><circle cx="15" cy="16" r="6"/><path d="M4 36c0-7 5-11 11-11s11 4 11 11"/><rect x="24" y="4" width="13" height="10" rx="1"/><path d="M27 8h7M27 11h5"/></svg><span class="step__num">1</span></div><p class="step__label">Request a Quote</p></div>
    <div class="step" style="left:212px"><div class="step__ring"><svg width="40" height="40" viewBox="0 0 40 40" fill="none" stroke="#fff" stroke-width="1.5"><rect x="3" y="7" width="34" height="22" rx="2"/><path d="M3 9l17 12 17-12"/><circle cx="20" cy="30" r="7" fill="#1b3f9d"/><path d="M20 26v7M17 30l3 3 3-3"/></svg><span class="step__num">2</span></div><p class="step__label">Receive a Quote</p></div>
    <div class="step" style="left:382px"><div class="step__ring"><svg width="40" height="40" viewBox="0 0 40 40" fill="none" stroke="#fff" stroke-width="1.5"><rect x="18" y="4" width="18" height="26" rx="1"/><path d="M22 12h10M22 17h10M22 22h8"/><path d="M4 20l8-4 8 4v10l-8 4-8-4z" fill="#1b3f9d"/><path d="M4 20l8 4 8-4M12 24v10"/></svg><span class="step__num">3</span></div><p class="step__label">Convert a Quote to order</p></div>
    <span class="btn btn--primary" style="left:196px;top:230px;width:104px">Request a quote</span>
    <span class="btn btn--ghost" style="left:311px;top:230px;width:92px">Catalog</span>
  </section>

  <section class="section blog">
    <h2 class="h2 h2--center" style="top:40px">Latest blog</h2>
    <article class="post" style="left:55px"><div class="post__img" role="img" aria-label="Greyscale photo of an angle grinder throwing sparks" style="background:linear-gradient(120deg,#2e2e2e,#8a8a8a 45%,#e0e0e0 62%,#3a3a3a)"></div><h3 class="post__title">At vero eos et accusamus et iusto odio dignis</h3><p class="post__meta"><b>&#9679;</b> 15/02/2022 &nbsp;|&nbsp; <b>&#9632;</b> Mara Quill</p><p class="post__text">Neque porro quisquam est, qui dolo rem ipsum quia dolor sit amet, cons ectetam est, qturdipisci.</p><p class="post__more">Read more</p></article>
    <article class="post" style="left:220px"><div class="post__img" role="img" aria-label="Greyscale photo of caster wheels on a shelf" style="background:linear-gradient(110deg,#2a2a2a,#5a5a5a 30%,#9a9a9a 55%,#7c7c7c 80%,#4a4a4a)"></div><h3 class="post__title">At vero eos et accusamus et iusto odio dignis</h3><p class="post__meta"><b>&#9679;</b> 15/02/2022 &nbsp;|&nbsp; <b>&#9632;</b> Mara Quill</p><p class="post__text">Neque porro quisquam est, qui dolo rem ipsum quia dolor sit amet, cons ectetam est, qturdipisci.</p><p class="post__more">Read more</p></article>
    <article class="post" style="left:385px"><div class="post__img" role="img" aria-label="Greyscale photo of a fixed caster on a cart" style="background:linear-gradient(180deg,#7d7d7d,#bdbdbd 55%,#d4d4d4 80%,#e8e8e8)"></div><h3 class="post__title">At vero eos et accusamus et iusto odio dignis</h3><p class="post__meta"><b>&#9679;</b> 15/02/2022 &nbsp;|&nbsp; <b>&#9632;</b> Mara Quill</p><p class="post__text">Neque porro quisquam est, qui dolo rem ipsum quia dolor sit amet, cons ectetam est, qturdipisci.</p><p class="post__more">Read more</p></article>
  </section>

  <footer class="section footer">
    <div class="brand"><span class="brand__dot"></span>ROLLVANE SUPPLY .com</div>
    <div class="f-col" style="left:259px"><h4>Quick Links</h4><ul><li>Home</li><li>Contact Us</li><li>About</li><li>Resources</li><li>Blog</li><li>Privacy Policy</li></ul></div>
    <div class="f-col" style="left:377px"><h4>Contact Us</h4>
      <div class="f-contact"><svg width="6" height="8" viewBox="0 0 6 8"><path d="M3 0a3 3 0 0 1 3 3c0 2-3 5-3 5S0 5 0 3a3 3 0 0 1 3-3z" fill="#3c7ede"/></svg><span>At vero eos et accusamus et iust dignissimos ducimus qu</span></div>
      <div class="f-contact"><svg width="7" height="7" viewBox="0 0 10 10"><path d="M2 0.5l2 2-1 1.3c.6 1.3 1.6 2.3 2.9 2.9L7.2 5.7l2.3 2-1.2 1.8C4.5 9.3 0.7 5.5 0.5 1.7z" fill="#3c7ede"/></svg><span>1 800 555 0142</span></div>
      <div class="f-contact"><svg width="8" height="6" viewBox="0 0 8 6"><rect width="8" height="6" fill="#3c7ede"/><path d="M0 0l4 3 4-3" stroke="#242424" fill="none" stroke-width=".8"/></svg><span>info@rollvanesupply.com</span></div>
    </div>
    <div class="f-rule"></div>
    <p class="copy">©2022 Rollvane Supply. All rights reserved.</p>
    <span class="social" style="left:474px"></span><span class="social" style="left:497px"></span><span class="social" style="left:520px"></span>
  </footer>
</main>

</body>
</html>
```